Building Company Business Card Design

Need a design for a business card:
It needs to have: Name, Phone, Facebook link, Website, email
i would also like a list of works we undertake:
-New Homes
-Extensions, Renovations & Bathrooms
-Decking, Carports, Sheds (Residential and Industrial)
-Carpentry
-Fences, Patios & Pergolas

Name, Phone, Facebook link, Website, email + details of services provided listed in description

```html
<!DOCTYPE html>
<html lang="en">
<head>
<meta charset="utf-8">
<title>Ridgeline Homes – Business Card</title>
<link href="https://fonts.googleapis.com/css2?family=Montserrat:wght@400;500;600;700;800&display=swap" rel="stylesheet">
<style>
  :root {
    --green: #39b54a;
    --green-soft: #e9f5ec;
    --ink: #1b1b1b;
    --card-dark: #181818;
    --grey: #8c8c8c;
    --grey-light: #ececec;
    --white: #ffffff;
    --backdrop: #2a2a2a;
  }
  * { box-sizing: border-box; margin: 0; padding: 0; }
  html, body { width: 1200px; height: 900px; overflow: hidden; }
  body {
    background: var(--backdrop);
    font-family: "Montserrat", sans-serif;
    display: flex;
    align-items: center;
    justify-content: center;
    gap: 40px;
  }
  .card {
    position: relative;
    width: 540px;
    height: 309px;
    border-radius: 14px;
    overflow: hidden;
  }

  /* Back side */
  .card--back { background: var(--card-dark); color: var(--white); }
  .brand {
    text-transform: uppercase;
    font-weight: 700;
    letter-spacing: 0.04em;
    line-height: 1;
  }
  .card--back .brand {
    position: absolute;
    top: 70px; left: 0; right: 0;
    text-align: center;
    color: var(--white);
  }
  .brand__name { font-size: 40px; display: flex; align-items: center; justify-content: center; gap: 12px; }
  .brand__mark { width: 16px; height: 16px; background: var(--green); display: inline-block; }
  .brand__sub { font-size: 15px; margin-top: 6px; letter-spacing: 0.12em; }

  .services {
    position: absolute;
    left: 40px; right: 40px; top: 182px;
    text-align: center;
  }
  .services__rule {
    display: flex; align-items: center; gap: 12px;
    color: var(--green); font-weight: 800; font-size: 13px; letter-spacing: 0.06em;
  }
  .services__rule::before, .services__rule::after {
    content: ""; flex: 1; height: 1.5px; background: var(--green);
  }
  .services__list { margin-top: 14px; font-size: 12.5px; font-weight: 500; line-height: 1.7; }
  .dot { color: var(--green); margin: 0 5px; }

  /* Front side */
  .card--front { background: var(--white); color: var(--ink); }
  .card--front .brand {
    position: absolute; top: 40px; left: 40px;
    color: var(--ink);
  }
  .card--front .brand__name { font-size: 28px; justify-content: flex-start; }
  .card--front .brand__sub { font-size: 10.5px; }

  .accent-bar { position: absolute; left: 0; top: 142px; width: 14px; height: 46px; background: var(--green); }
  .person { position: absolute; left: 36px; top: 140px; }
  .person__name { color: var(--green); font-weight: 800; font-size: 26px; letter-spacing: 0.03em; text-transform: uppercase; }
  .person__role { font-size: 14px; font-weight: 500; margin-top: 2px; }

  .contact { position: absolute; left: 48px; top: 206px; list-style: none; font-size: 13px; font-weight: 500; }
  .contact li { display: flex; align-items: center; gap: 9px; height: 20px; }
  .contact svg { width: 12px; height: 12px; flex: none; }

  .corner { position: absolute; right: 0; bottom: 0; width: 300px; height: 309px; }
</style>
</head>
<body>

<section class="card card--back">
  <div class="brand">
    <div class="brand__name"><span class="brand__mark"></span>Ridgeline Homes</div>
    <div class="brand__sub">And Developments Pty Ltd</div>
  </div>
  <div class="services">
    <div class="services__rule">OUR SERVICES</div>
    <p class="services__list">
      New Homes<span class="dot">•</span>Extensions, Renovations &amp; Bathrooms<span class="dot">•</span>Carpentry<br>
      Decking, Carports, Sheds<span class="dot">•</span>Fences, Patios &amp; Pergolas
    </p>
  </div>
</section>

<section class="card card--front">
  <svg class="corner" viewBox="0 0 300 309" aria-hidden="true">
    <polygon points="300,210 300,309 70,309 90,285" fill="var(--green)"/>
    <polygon points="90,285 70,309 0,309 0,300" fill="var(--grey)"/>
  </svg>
  <div class="brand">
    <div class="brand__name">Ridgeline Homes</div>
    <div class="brand__sub">And Developments Pty Ltd</div>
  </div>
  <span class="accent-bar"></span>
  <div class="person">
    <h1 class="person__name">Mark Ellison</h1>
    <p class="person__role">Managing Director</p>
  </div>
  <ul class="contact">
    <li>
      <svg viewBox="0 0 12 12"><path d="M2 1h3l1 3-2 1a7 7 0 0 0 3 3l1-2 3 1v3a1 1 0 0 1-1 1A10 10 0 0 1 1 2a1 1 0 0 1 1-1z" fill="var(--green)"/></svg>
      555-014-2276
    </li>
    <li>
      <svg viewBox="0 0 12 12"><rect x="0.5" y="2" width="11" height="8" rx="1" fill="var(--green)"/><path d="M1 3l5 4 5-4" stroke="#fff" fill="none"/></svg>
      info@ridgelinehomespty.com
    </li>
    <li>
      <svg viewBox="0 0 12 12"><circle cx="6" cy="6" r="5.3" fill="none" stroke="var(--green)" stroke-width="1.2"/><path d="M1 6h10M6 1c-3 3-3 7 0 10M6 1c3 3 3 7 0 10" stroke="var(--green)" fill="none"/></svg>
      www.ridgelinehomespty.com
    </li>
    <li>
      <svg viewBox="0 0 12 12"><circle cx="6" cy="6" r="6" fill="var(--green)"/></svg>
      @ridgelinehomespty
    </li>
  </ul>
</section>

</body>
</html>
```